Kelp Webcomic

A simple signup landing page and blog design for an upcoming webcomic. I am mostly looking for a flat UI with a simple color scheme. I want to showcase a large background image and the comic title image. I have all the technicals figured out (I am a web developer by trade), so all I need now is a solid design I like.

The signup for should only have one field (email) and have text above it, and smaller text below it.

The blog, I am thinking, should be in the style of comic book pages. The home page would be blocks with large white outlines, with the article pages being an extension of that. As I stated before, should be fairly minimalist, but fun. Also, no sidebar or ads, IE single column. I have attached a simple mockup/layout of the blog to give a general idea of what I am going for.

I have attached the Logo and Background art (uncolored) for reference. Don't worry about the background image blending in, I can take care of that when the design is implemented. I will be focusing on layout and overall look, not necessarily readability (which I can fix).

~Please DO NOT take these examples literally. I will describe what I like about each example.~

Signup pages:
http://example-plinth.com/landing-page-type-photo/
http://www.example-varnoq.com/showcase/website-design/814/10-most-beautiful-landing-pages-in-minimalist-style
http://example-quellbay.com/47-modern-landing-pages-showcasing-inspirational-web-design/
Great examples of minimalist design. However, instead of text or other content, there should be a simple signup form, as described above. Also think a lot more "playful" rather than super professional.

Blog:
http://example-vradd.no/
Awesome example of a single column, minimal design. Needs to be more "comicbook style" though.
http://example-tumbrik.com/
Another good example of minimal design blog.
http://example-morvane.net/wp-content/uploads/res-blogs-5.jpg
I like the timeline feel here. Combine that with a comic book page kind of thing, and I think you have a winner.

Actual webcomic landing (not required):
http://www.example-fennowhistle.com/comic.php?date=20021104#.U90ysYBdUvU
I like the navigation. It makes the atmosphere nice for the comic. The page layout itself is WAY too busy.
http://www.example-lodgeworth.com/comic/
Fairly common webcomic, but their navigation and page layout is nice.
http://example-qwib.com/936/
Another common webcomic. The simple page layout makes it easy for people to get started I think.

So there you have it. I will try my best to keep updating and adding to the description. If you have any questions, please don't hesitate to ask.

Hey Guys, I am really appreciating all the effort you have been putting in. I am amazed to see all the awesome designs and all the care taken with the project. I am just writing everyone to let you know that I have uploaded a simple layout/wireframe of the blog, to give an idea of what I am going for. Can't wait to see how things progress, and good luck to everyone!

Industry/Entity Type

Trade

Font styles to use
Sans Serif

Requirements
Must have
• Must showcase a large background image (does not have to cover the entire background). Should be a flat UI as well. Should be mostly neutral with splashes of blue or purple. Social links should also be somewhere (twitter, facebook, etc.).
Nice to have
• I am thinking something with rounded boxes, but I can live without them. A more "fun" design as opposed to more professional is definitely nice to have.

If you would like to try a stab at the actual comic page display and navigation, you are welcome to submit something. It should not be a main priority though.

Being responsive is not a requirement, but it would be nice to have.
Should not have
• A billion links in the navigation or look too busy.
No sidebar or advertisements. Should be a clean design.

```html
<!DOCTYPE html>
<html lang="en">
<head>
<meta charset="utf-8">
<title>Kelp Webcomic — Sign Up</title>
<link href="https://fonts.googleapis.com/css2?family=Courgette&family=Source+Sans+3:wght@400;600;700&display=swap" rel="stylesheet">
<style>
  :root {
    --bg: #000000;
    --panel: #f4f4f4;
    --panel-art-light: #efefef;
    --panel-art-dark: #d6d6d6;
    --purple: #663399;
    --purple-title: #5b2d91;
    --ink: #333333;
    --muted: #666666;
    --field-border: #9a9a9a;
    --placeholder: #9b9b9b;
    --white: #ffffff;
    --green: #5aa81e;
    --green-dark: #3f8412;
  }
  * { margin: 0; padding: 0; box-sizing: border-box; }
  html, body {
    width: 1200px; height: 676px; overflow: hidden;
    background: var(--bg);
    font-family: "Source Sans 3", "Source Sans Pro", sans-serif;
  }
  .canvas { position: relative; width: 1200px; height: 676px; }

  .signup-panel {
    position: absolute; left: 310px; top: 86px; width: 584px; height: 476px;
    border-radius: 28px;
    background: var(--panel);
    overflow: hidden;
  }
  .panel-art {
    position: absolute; inset: 0;
    background:
      radial-gradient(ellipse at 20% 60%, var(--panel-art-dark) 0%, transparent 45%),
      radial-gradient(ellipse at 85% 55%, var(--panel-art-dark) 0%, transparent 40%),
      linear-gradient(180deg, var(--panel-art-light), #e4e4e4);
    opacity: .8;
  }

  .brand {
    position: absolute; left: 0; width: 1200px; top: 40px;
    text-align: center;
    font-weight: 700; font-size: 58px; line-height: 76px;
    color: var(--purple);
    letter-spacing: 2px;
  }

  .title {
    position: absolute; left: 0; width: 1200px; top: 151px;
    text-align: center;
    font-family: "Courgette", cursive;
    font-size: 32px; line-height: 40px; font-weight: 400;
    color: var(--purple-title);
  }
  .subtitle {
    position: absolute; right: 397px; top: 188px;
    font-size: 12px; line-height: 15px; color: var(--ink);
  }
  .intro {
    position: absolute; left: 0; width: 1200px; top: 231px;
    text-align: center;
    font-size: 14px; line-height: 23px; font-weight: 600;
    color: var(--ink); text-transform: uppercase;
  }
  .email-field {
    position: absolute; left: 440px; top: 294px; width: 320px; height: 42px;
    border: 1px solid var(--field-border); border-radius: 3px;
    background: var(--white);
    font-size: 13px; color: var(--placeholder);
    display: flex; align-items: center; justify-content: center;
  }
  .signup-button {
    position: absolute; left: 440px; top: 360px; width: 320px; height: 42px;
    border-radius: 3px; background: var(--purple);
    color: var(--white); font-weight: 700; font-size: 15px;
    display: flex; align-items: center; justify-content: center;
    letter-spacing: .3px;
  }
  .fine-print {
    position: absolute; left: 438px; width: 324px; top: 421px;
    text-align: center; font-size: 12px; line-height: 19px; color: var(--muted);
  }

  .blog-arrow { position: absolute; left: 846px; top: 484px; width: 102px; height: 78px; }

  .social {
    position: absolute; top: 597px; left: 0; width: 1200px;
    display: flex; justify-content: center; gap: 7px;
    list-style: none;
  }
  .social li {
    width: 26px; height: 26px; border-radius: 50%; background: var(--white);
  }
  .social li.is-active { background: var(--green); }
  .copyright {
    position: absolute; top: 632px; left: 0; width: 1200px;
    text-align: center; font-size: 11px; line-height: 16px; color: var(--white);
  }
</style>
</head>
<body>
<main class="canvas">
  <section class="signup-panel">
    <div class="panel-art" role="img" aria-label="Uncoloured line-art background illustration of comic characters and a hillside town"></div>
  </section>

  <div class="brand">Kelp</div>

  <h1 class="title">Sign up For a Kelp webcomic</h1>
  <p class="subtitle">Get free comics like Zerravane, Quillmoth Saga, Brindlecrow and more!</p>

  <p class="intro">Start amassing a Kelp webcomic and be<br>the envy of your friends and foes alike!</p>

  <div class="email-field">Enter your email</div>
  <div class="signup-button">SIGN UP</div>

  <p class="fine-print">Lorem ipsum dolor sit amet, consectetur adipisicing elit, sed do eius mod tempor incididunt ut labore et dolore magna aliqua. Ut enim ad minim veniam, quis nostrud exercitation ullamco laboris nisi ut aliquip ex ea commodo consequat.</p>

  <svg class="blog-arrow" viewBox="0 0 104 80" aria-label="Our blog">
    <path d="M4 22 L56 18 L54 4 L100 40 L56 76 L56 60 L10 58 Z" fill="var(--white)"/>
    <path d="M10 27 L62 24 L61 13 L92 40 L62 67 L62 54 L14 52 Z" fill="var(--green)"/>
    <path d="M14 46 L62 48 L62 54 L14 52 Z" fill="var(--green-dark)"/>
    <text x="48" y="36" text-anchor="middle" font-family="Source Sans 3, sans-serif" font-weight="700" font-size="10" fill="var(--white)">OUR</text>
    <text x="48" y="49" text-anchor="middle" font-family="Source Sans 3, sans-serif" font-weight="700" font-size="13" fill="var(--white)">BLOG</text>
  </svg>

  <ul class="social" aria-label="Social links">
    <li></li><li></li><li class="is-active"></li><li></li><li></li><li></li>
  </ul>
  <p class="copyright">Copyright © 2014 Kelp Webcomic All rights reserved.</p>
</main>
</body>
</html>
```